Counselling business requires poster

I require a poster to promote my counselling and coaching business I will be placing these in doctors surgery's and clinics etc.
This business is centred around helping people work through emotional issues. We provided one on one sessions which help enhance peoples lives by assisting them in overcoming their fears, obsessions, insecurities etc.

We offer support in a broad range of areas:

- Eating disorders & weight managment
- Depression
- Marriage and relationship issues
- Anxiety
- Victims of physical, verbal and/or social abuse

We want our poster to be representative of the positive, warm and welcoming atmosphere we provide.

Our motto, 'One step at a time', is symbolic of our approach and how we help our clients to tackle their problems bit by bit.

The flyer I have uploaded is just some information on what we offer

Thankyou for your designs I am taking them into consideration and will inform you of any decision.

Weight

```html
<!DOCTYPE html>
<html lang="en">
<head>
<meta charset="utf-8">
<title>One Step at a Time – Counselling Poster</title>
<link rel="stylesheet" href="https://fonts.googleapis.com/css2?family=Nanum+Pen+Script&family=Crimson+Pro:wght@400&display=swap">
<style>
  :root {
    --backdrop: #1f6e98;
    --paper: #ffffff;
    --ink-plum: #2b0f2c;
    --ink-text: #2a2a2a;
    --sky-top: #f7eef4;
    --sky-glow: #fdf3e2;
    --sun-yellow: #f7c531;
    --sun-orange: #f0a13a;
    --field-green: #a9bd4c;
    --field-deep: #7fa03c;
  }
  * { margin: 0; padding: 0; box-sizing: border-box; }
  html, body {
    width: 1009px;
    height: 1200px;
    overflow: hidden;
    background: var(--backdrop);
  }
  .poster {
    position: absolute;
    left: 114px;
    top: 196px;
    width: 781px;
    height: 808px;
    background: var(--paper);
    overflow: hidden;
  }
  .hero-photo {
    position: absolute;
    left: 0; top: 0;
    width: 781px;
    height: 681px;
    background: linear-gradient(180deg, var(--sky-top) 0%, var(--sky-glow) 55%, var(--sun-orange) 70%, var(--sun-yellow) 78%, var(--field-green) 90%, var(--field-deep) 100%);
  }
  .headline {
    position: absolute;
    font-family: "Nanum Pen Script", cursive;
    color: var(--ink-plum);
    font-weight: 400;
    line-height: 1;
    white-space: nowrap;
  }
  .headline--main {
    left: 114px;
    top: 272px;
    font-size: 146px;
    letter-spacing: 1px;
  }
  .headline--sub {
    left: 280px;
    top: 406px;
    font-size: 62px;
    letter-spacing: 3px;
  }
  .services-band {
    position: absolute;
    left: 0; top: 681px;
    width: 781px;
    height: 62px;
    background: var(--paper);
  }
  .services-list {
    position: absolute;
    right: 145px;
    top: 12px;
    font-family: "Crimson Pro", serif;
    font-size: 15px;
    line-height: 19px;
    color: var(--ink-text);
    text-align: right;
    white-space: nowrap;
  }
  .services-list .divider { padding: 0 8px; }
  .brand-name {
    position: absolute;
    left: 676px;
    top: 21px;
    font-family: "Crimson Pro", serif;
    font-size: 15px;
    color: var(--ink-plum);
    display: flex;
    align-items: center;
    gap: 4px;
  }
  .brand-name .brand-dot {
    width: 9px; height: 9px;
    border-radius: 50%;
    background: var(--sun-orange);
  }
  .contact-strip {
    position: absolute;
    left: 0; top: 743px;
    width: 781px;
    height: 65px;
    background: linear-gradient(90deg, var(--field-green) 0%, var(--sun-yellow) 30%, var(--sun-orange) 60%, var(--sun-orange) 100%);
  }
  .contact-line {
    position: absolute;
    top: 17px;
    font-family: "Nanum Pen Script", cursive;
    font-size: 30px;
    line-height: 1;
    color: var(--ink-plum);
    letter-spacing: 1px;
    white-space: nowrap;
  }
  .contact-line--phone { left: 98px; }
  .contact-line--web { right: 92px; }
</style>
</head>
<body>
  <main class="poster">
    <div class="hero-photo" role="img" aria-label="Photograph of a joyful woman in a white dress with arms outstretched in a sunlit meadow"></div>

    <h1 class="headline headline--main">One Step</h1>
    <p class="headline headline--sub">at a Time</p>

    <section class="services-band">
      <p class="services-list">
        Eating disorders &amp; weight managment<span class="divider">|</span>Marriage and relationship issues<br>
        Depression<span class="divider">|</span>Anxiety<span class="divider">|</span>Victims of physical, verbal and/or social abuse
      </p>
      <div class="brand-name"><span class="brand-dot"></span>Pathways</div>
    </section>

    <footer class="contact-strip">
      <span class="contact-line contact-line--phone">call 08 555 0142</span>
      <span class="contact-line contact-line--web">www.pathwayshub.com</span>
    </footer>
  </main>
</body>
</html>
```